Interior Stylist business card design needed

I need a business card for my new company in Sydney called "Lu Brannigan Designs". The business offers an interior styling and colour consultancy. My clients are generally not very design savvy (hence why they use me) and can range from being quite conservative to really wanting something "out there". They can be looking for a budget makeover or something more expensive / substantial. I'd like my business card design to be stylish (but not overly formal). I certainly don't want it to be conservative. I'd like it to stand out a bit! I don't really have any aversion to particular colours and I don't have a logo as such - my business name is really all I have.

Target Market(s)

As above - home owners, ranging from conservative to modern

Industry/Entity Type

Conservative

Contact Information for Business Card

Lu Brannigan Designs
Colour consultancy and interior styling
ph: 0417 368 205
email: lubrannigan@zephmail.net.au

Requirements
Should not have
• Old fashioned writing or motifs. No Times Roman font!!

```html
<!DOCTYPE html>
<html lang="en">
<head>
<meta charset="utf-8">
<title>Lu Brannigan Designs – Business Card</title>
<link rel="stylesheet" href="https://fonts.googleapis.com/css2?family=Sacramento&family=Josefin+Sans:wght@300;400;600&display=swap">
<style>
  :root {
    --page-bg: #1c1d1e;
    --card-top: #34383a;
    --card-bottom: #25282a;
    --name-ink: #e2dcd1;
    --suffix-ink: #b9b4ab;
    --tagline-ink: #c9c4bb;
    --band: #0b0b0c;
    --contact-ink: #c4c6c7;
    --ornament: #1a1c1d;
  }
  * { box-sizing: border-box; margin: 0; padding: 0; }
  html, body {
    width: 1200px; height: 900px; overflow: hidden;
    background: var(--page-bg);
  }
  .canvas { position: relative; width: 1200px; height: 900px; }
  .card {
    position: absolute; left: 290px; width: 620px; height: 354px;
    border-radius: 18px;
    background: linear-gradient(160deg, var(--card-top), var(--card-bottom));
    box-shadow: 0 12px 30px rgba(0,0,0,.55);
    overflow: hidden;
  }
  .card--front { top: 70px; }
  .card--back { top: 476px; }

  .ornament {
    position: absolute; left: 50%; transform: translateX(-50%);
    background: var(--ornament);
    border-radius: 40px;
  }
  .wordmark {
    position: absolute; left: 0; right: 0; text-align: center;
    font-weight: 400;
  }
  .wordmark__name {
    display: block;
    font-family: "Sacramento", cursive;
    font-weight: 400;
    line-height: 1;
    color: var(--name-ink);
  }
  .wordmark__suffix {
    display: block;
    font-family: "Josefin Sans", sans-serif;
    font-weight: 600;
    letter-spacing: .34em;
    padding-left: .34em;
    color: var(--suffix-ink);
  }

  /* Front */
  .card--front .ornament--top { top: 52px; width: 250px; height: 40px; }
  .card--front .ornament--bottom { top: 262px; width: 250px; height: 40px; }
  .card--front .wordmark { top: 112px; }
  .card--front .wordmark__name { font-size: 92px; }
  .card--front .wordmark__suffix { font-size: 24px; margin-top: 6px; }

  /* Back */
  .tagline {
    position: absolute; left: 34px; top: 26px;
    font-family: "Sacramento", cursive;
    font-size: 32px; line-height: 1.2; color: var(--tagline-ink);
  }
  .card--back .ornament--top { top: 92px; width: 170px; height: 26px; }
  .card--back .ornament--bottom { top: 218px; width: 170px; height: 26px; }
  .card--back .wordmark { top: 126px; }
  .card--back .wordmark__name { font-size: 56px; }
  .card--back .wordmark__suffix { font-size: 15px; margin-top: 4px; }

  .contact-band {
    position: absolute; left: 0; right: 0; top: 262px; height: 52px;
    background: var(--band);
    display: flex; align-items: center; justify-content: space-between;
    padding: 0 40px;
    font-family: "Josefin Sans", sans-serif;
    font-weight: 300;
    font-size: 18px; color: var(--contact-ink);
    letter-spacing: .04em;
  }
  .contact-item { display: flex; align-items: center; gap: 12px; line-height: 1; }
  .contact-item svg { width: 17px; height: 17px; fill: var(--contact-ink); }
  .contact-item__at { font-weight: 400; }
</style>
</head>
<body>
<main class="canvas">

  <section class="card card--front" aria-label="Card front">
    <div class="ornament ornament--top" role="img" aria-label="Decorative scroll flourish"></div>
    <h1 class="wordmark">
      <span class="wordmark__name">Lu Brannigan</span>
      <span class="wordmark__suffix">DESIGNS</span>
    </h1>
    <div class="ornament ornament--bottom" role="img" aria-label="Decorative scroll flourish"></div>
  </section>

  <section class="card card--back" aria-label="Card back">
    <p class="tagline">Colour consultancy and interior styling</p>
    <div class="ornament ornament--top" role="img" aria-label="Decorative scroll flourish"></div>
    <h2 class="wordmark">
      <span class="wordmark__name">Lu Brannigan</span>
      <span class="wordmark__suffix">DESIGNS</span>
    </h2>
    <div class="ornament ornament--bottom" role="img" aria-label="Decorative scroll flourish"></div>

    <div class="contact-band">
      <span class="contact-item">
        <svg viewBox="0 0 24 24" aria-hidden="true"><path d="M6.6 10.8a15.1 15.1 0 0 0 6.6 6.6l2.2-2.2a1 1 0 0 1 1-.25 11.4 11.4 0 0 0 3.6.57 1 1 0 0 1 1 1V20a1 1 0 0 1-1 1A17 17 0 0 1 3 4a1 1 0 0 1 1-1h3.5a1 1 0 0 1 1 1c0 1.25.2 2.45.57 3.57a1 1 0 0 1-.25 1z"/></svg>
        0417 368 205
      </span>
      <span class="contact-item">
        <span class="contact-item__at">@</span>
        lubrannigan@zephmail.net.au
      </span>
    </div>
  </section>

</main>
</body>
</html>
```